Electronic Time-sheet for phones

I need a time-sheet that can be accessed on the phone, be completed, then have the ability to electronically sign. The time sheet needs to be used two fold for supervision to verify hours and quantities and also for the client to be able to electronically sign. The time-sheet should be daily or weekly if we can get the data to fit. We are trying to streamline field supervisors having to log on to a computer to access a server just to do time-sheets. We need it to be user friendly. We need to have two places to have electronic signatures. One for supervisor or authorized representative and the other for the client to sign.

Target Market(s)

Industrial clients

Industry/Entity Type

Oil And Gas

Requirements
Must have
• hours, quantities, project name, location, signature line etc
Nice to have
• n/a
Should not have
• n/a

```html
<!DOCTYPE html>
<html lang="en">
<head>
<meta charset="utf-8">
<title>Kestrel Daily Time-sheet</title>
<link href="https://fonts.googleapis.com/css2?family=Roboto:wght@400;500;700;900&display=swap" rel="stylesheet">
<style>
  :root {
    --page-bg: #3daeff;
    --header-bg: #142a55;
    --bar-bg: #050b18;
    --body-bg: #0b1529;
    --rule: #1c2a45;
    --white: #ffffff;
    --muted: #c9cfdb;
    --row-text: #9aa3b5;
    --label-gold: #e6deaa;
    --total-yellow: #f1ec7a;
    --bubble-green: #8ee06a;
    --bubble-blue: #6f97d8;
  }
  * { margin: 0; padding: 0; box-sizing: border-box; }
  html, body { width: 1200px; height: 1200px; overflow: hidden; }
  body {
    background: var(--page-bg);
    font-family: "Roboto", Arial, sans-serif;
    position: relative;
  }
  .screen {
    position: absolute;
    left: 319px; top: 29px;
    width: 610px; height: 1240px;
    transform: scale(0.92);
    transform-origin: top left;
    background: var(--body-bg);
    border-radius: 56px;
    overflow: hidden;
  }
  .abs { position: absolute; }
  .app-header { left: 0; top: 0; width: 610px; height: 177px; background: var(--header-bg); }
  .menu-icon { left: 40px; top: 76px; }
  .brand {
    left: 0; width: 610px; top: 58px; text-align: center;
    color: var(--white); font-weight: 900; font-size: 44px; letter-spacing: 1px;
  }
  .login { left: 490px; top: 62px; display: flex; align-items: center; gap: 9px; color: var(--white); font-size: 12px; letter-spacing: .5px; }
  .header-rule { left: 40px; top: 123px; width: 523px; height: 1px; background: #3a5282; }
  .client-name { left: 0; width: 610px; top: 132px; text-align: center; color: var(--white); font-size: 14px; letter-spacing: 1.6px; font-weight: 500; }
  .client-site { left: 0; width: 610px; top: 154px; text-align: center; color: var(--label-gold); font-size: 10.5px; letter-spacing: 1.5px; }

  .info-bar { left: 0; top: 177px; width: 610px; height: 51px; background: var(--bar-bg); color: var(--muted); font-size: 11.5px; letter-spacing: .8px; }
  .info-bar .item { position: absolute; top: 0; height: 51px; display: flex; align-items: center; gap: 10px; }
  .info-bar .value { color: var(--white); letter-spacing: .3px; font-size: 12px; }
  .signature { width: 66px; height: 26px; border-radius: 3px; background: linear-gradient(90deg, #2a3550, #4a5570); }

  .field-label { left: 40px; color: var(--white); font-size: 12px; letter-spacing: 1px; font-weight: 500; }
  .description-box { left: 40px; top: 282px; width: 525px; height: 92px; border: 1px solid var(--rule); }
  .code-rule { left: 40px; top: 458px; width: 523px; height: 1px; background: var(--rule); }
  .full-rule { left: 0; width: 610px; height: 1px; background: var(--rule); }
  .table-rule { left: 10px; width: 600px; height: 1px; background: var(--rule); }

  .timesheet { left: 0; top: 516px; width: 610px; border-collapse: collapse; }
  .timesheet th { color: var(--label-gold); font-size: 11.5px; letter-spacing: 1px; font-weight: 700; text-align: left; height: 22px; padding: 0; }
  .timesheet td { color: var(--row-text); font-size: 12px; letter-spacing: .3px; height: 30.6px; padding: 0; }
  .timesheet thead tr { height: 46px; }
  .timesheet tbody tr:first-child td { padding-top: 0; }
  .col-name { width: 145px; padding-left: 41px !important; }
  .col-class { width: 170px; }
  .col-emp { width: 110px; }
  .col-hours { width: 99px; }
  .spacer td { height: 12px !important; }

  .totals { left: 57px; width: 480px; color: var(--white); font-size: 17px; letter-spacing: 1px; }
  .totals .num { position: absolute; top: 0; color: var(--total-yellow); letter-spacing: .5px; }

  .comments {
    left: 249px; top: 1088px; width: 122px; height: 122px; border-radius: 50%;
    background: var(--white); border: 5px solid #16284a;
    display: flex; flex-direction: column; align-items: center; justify-content: center; gap: 2px;
    color: #333; font-size: 12px; letter-spacing: .8px;
  }
</style>
</head>
<body>
  <main class="screen">
    <header class="abs app-header">
      <svg class="abs menu-icon" width="28" height="20" viewBox="0 0 28 20">
        <rect x="0" y="0" width="28" height="2" fill="#fff"/>
        <rect x="0" y="8" width="24" height="2" fill="#fff"/>
        <rect x="0" y="16" width="18" height="2" fill="#fff"/>
      </svg>
      <div class="abs brand">KESTREL</div>
      <div class="abs login">
        <svg width="30" height="30" viewBox="0 0 30 30" fill="none" stroke="#fff" stroke-width="1.5">
          <circle cx="15" cy="15" r="13.5"/>
          <circle cx="15" cy="11.5" r="5"/>
          <path d="M6 24c2-4.5 5.5-6.5 9-6.5s7 2 9 6.5"/>
        </svg>
        <span>Login</span>
      </div>
      <div class="abs header-rule"></div>
      <div class="abs client-name">NORTHFIELD CHEMICAL, INC.</div>
      <div class="abs client-site">NEW UNIT#1, CANADA</div>
    </header>

    <section class="abs info-bar">
      <div class="item" style="left:28px">FOREMAN : <span class="value">Alan Reed</span></div>
      <div class="item" style="left:239px">APPROVED BY : <span class="signature" role="img" aria-label="Handwritten approval signature"></span></div>
      <div class="item" style="left:472px">DATE: <span class="value">11-08-2018</span></div>
    </section>

    <div class="abs field-label" style="top:255px">DESCRIPTION OF WORK PERFORMED</div>
    <div class="abs description-box"></div>
    <div class="abs field-label" style="top:411px">COST / PHASE CODE</div>
    <div class="abs code-rule"></div>
    <div class="abs full-rule" style="top:503px"></div>

    <table class="abs timesheet">
      <thead>
        <tr><th class="col-name">NAME</th><th class="col-class">CLASS</th><th class="col-emp">EMP NO.</th><th class="col-hours">HOURS</th><th>TOTAL</th></tr>
      </thead>
      <tbody>
        <tr class="spacer"><td colspan="5"></td></tr>
        <tr><td class="col-name">Liam</td><td>Daily Quantities</td><td>1547</td><td>5</td><td>15</td></tr>
        <tr><td class="col-name">Lucas</td><td>Daily Quantities</td><td>1234</td><td>10</td><td>30</td></tr>
        <tr><td class="col-name">Elizabeth</td><td>Daily Quantities</td><td>1537</td><td>8</td><td>24</td></tr>
        <tr><td class="col-name">Michael</td><td>Daily Quantities</td><td>2323</td><td>12</td><td>36</td></tr>
        <tr><td class="col-name">Liam</td><td>Daily Quantities</td><td>1867</td><td>15</td><td>45</td></tr>
        <tr><td class="col-name">Lucas</td><td>Daily Quantities</td><td>1436</td><td>7</td><td>21</td></tr>
        <tr><td class="col-name">Elizabeth</td><td>Daily Quantities</td><td>2130</td><td>6</td><td>20</td></tr>
        <tr><td class="col-name">Michael</td><td>Daily Quantities</td><td>1865</td><td>15</td><td>45</td></tr>
        <tr><td class="col-name">Liam</td><td>Daily Quantities</td><td>2103</td><td>7</td><td>21</td></tr>
        <tr><td class="col-name">Lucas</td><td>Daily Quantities</td><td>1754</td><td>12</td><td>36</td></tr>
        <tr><td class="col-name">Elizabeth</td><td>Daily Quantities</td><td>1248</td><td>11</td><td>33</td></tr>
        <tr><td class="col-name">Michael</td><td>Daily Quantities</td><td>1537</td><td>10</td><td>30</td></tr>
        <tr><td class="col-name">Liam</td><td>Daily Quantities</td><td>1836</td><td>9</td><td>21</td></tr>
        <tr><td class="col-name">Lucas</td><td>Daily Quantities</td><td>2013</td><td>4</td><td>12</td></tr>
      </tbody>
    </table>
    <div class="abs table-rule" style="top:549px"></div>
    <div class="abs table-rule" style="top:1002px"></div>

    <div class="abs totals" style="top:1025px">HOUR TOTALS<span class="num" style="left:361px">134</span><span class="num" style="left:448px">768</span></div>
    <div class="abs totals" style="top:1060px">QUANTITY TOTALS<span class="num" style="left:361px">100</span><span class="num" style="left:448px">768</span></div>
    <div class="abs full-rule" style="top:1104px"></div>

    <div class="abs comments">
      <svg width="58" height="48" viewBox="0 0 58 48">
        <rect x="16" y="0" width="40" height="30" fill="var(--bubble-blue)"/>
        <path d="M2 10h40v26H14l-8 8v-8H2z" fill="var(--bubble-green)"/>
        <circle cx="13" cy="23" r="2.2" fill="#fff"/>
        <circle cx="22" cy="23" r="2.2" fill="#fff"/>
        <circle cx="31" cy="23" r="2.2" fill="#fff"/>
      </svg>
      <span>Comments</span>
    </div>
  </main>
</body>
</html>
```